Webdesign für Physiotherapie
Zielgruppe
Physiotherapie unter ganzheitlichen oder umfangreicheren Gesichtspunkten.
ANLAGE BEACHTEN!
Aufgabenstellung
Siehe Anlage!

```html
<!DOCTYPE html>
<html lang="de">
<head>
<meta charset="utf-8">
<title>Physiotherapie – Startseite</title>
<link rel="stylesheet" href="https://fonts.googleapis.com/css2?family=Outfit:wght@300;400;500;600;700;800&display=swap">
<style>
  :root{
    --gold:#d5ad14;
    --ink:#111111;
    --text:#2a2a2a;
    --white:#ffffff;
    --bg:#fafafa;
    --red:#e0322a;
    --note:#d2161e;
    --line:#9a9a9a;
  }
  *{box-sizing:border-box;margin:0;padding:0}
  html,body{width:1200px;height:890px;overflow:hidden;background:var(--bg);font-family:"Outfit",sans-serif;color:var(--text)}
  .page{position:relative;width:1200px;height:890px;overflow:hidden}

  .topbar{position:absolute;left:0;top:0;width:1200px;height:42px;background:var(--gold);color:var(--white);font-size:12.5px;font-weight:600}
  .topbar .item{position:absolute;top:13px;display:flex;align-items:center;gap:6px}
  .topbar .address{left:106px}
  .topbar .mail{right:93px}

  .header{position:absolute;left:0;top:42px;width:1200px;height:92px;background:var(--white)}
  .brand{position:absolute;left:98px;top:30px;display:flex;align-items:center;gap:8px;font-size:20px;font-weight:700;color:var(--gold)}
  .brand .dot{width:14px;height:14px;border-radius:50%;background:var(--gold)}
  .nav{position:absolute;left:253px;top:36px;display:flex;gap:27px;font-size:15.5px;font-weight:500;color:var(--ink)}
  .nav span{display:flex;align-items:center;gap:8px}
  .phone{position:absolute;right:100px;top:25px;display:flex;align-items:center;gap:12px;font-size:16px;font-weight:500;color:var(--ink)}
  .phone .ring{width:40px;height:40px;border-radius:50%;background:#eee;display:flex;align-items:center;justify-content:center}
  .phone .ball{width:30px;height:30px;border-radius:50%;background:var(--red);display:flex;align-items:center;justify-content:center}

  .hero-photo{position:absolute;left:440px;top:134px;width:760px;height:593px;
    background:linear-gradient(90deg,rgba(250,250,250,1) 0%,rgba(238,236,233,.9) 18%,#d7d2cd 40%,#c9b6a8 62%,#b98c7a 80%,#a6423d 100%)}
  .hero-leaves{position:absolute;left:0;top:300px;width:200px;height:420px;background:radial-gradient(ellipse at 20% 50%,rgba(170,180,175,.35),rgba(250,250,250,0) 70%)}

  .tagline{position:absolute;left:98px;top:206px;font-size:18.5px;color:var(--gold);font-weight:300}
  .tagline b{font-weight:700}
  .headline{position:absolute;left:98px;top:257px;border-left:4px solid var(--gold);padding-left:24px;height:111px;
    font-size:50px;font-weight:800;line-height:58px;color:var(--ink);letter-spacing:.5px}
  .intro{position:absolute;left:98px;top:390px;width:500px;font-size:14.5px;line-height:22.5px;font-weight:300;color:var(--text)}
  .btn{position:absolute;background:var(--gold);color:var(--white);font-weight:600;font-size:13.5px;border-radius:3px;display:flex;align-items:center;justify-content:center}
  .btn.book{left:98px;top:519px;width:136px;height:47px}

  .dropdown{position:absolute;left:252px;top:134px;width:203px;height:201px;background:var(--white);border-bottom:5px solid var(--gold);padding-top:14px}
  .dropdown li{list-style:none;display:flex;align-items:center;gap:10px;padding-left:20px;height:34px;font-size:15px;font-weight:500;color:var(--ink)}

  .note{position:absolute;left:98px;top:650px;font-size:14.5px;color:var(--note);font-weight:400}

  .infobox{position:absolute;left:98px;top:682px;width:1002px;height:151px;background:var(--white);border-radius:4px;box-shadow:0 6px 24px rgba(0,0,0,.06);overflow:hidden}
  .infobox .facts{position:absolute;left:0;top:0;width:454px;height:151px;background:var(--gold);color:var(--white)}
  .fact{position:absolute;top:22px;width:225px;text-align:center}
  .fact.loc{left:0}
  .fact.hours{left:225px}
  .fact h3{font-size:18px;font-weight:700;margin-top:6px}
  .fact p{font-size:15px;font-weight:300;line-height:22.5px;margin-top:6px}
  .facts .divider{position:absolute;left:232px;top:48px;width:1px;height:66px;background:rgba(255,255,255,.6)}
  .signup h3{position:absolute;left:494px;top:32px;font-size:18px;font-weight:700;color:var(--gold)}
  .signup .field{position:absolute;left:494px;top:92px;width:292px;padding-bottom:10px;border-bottom:1px solid var(--line);font-size:15px;font-weight:300;color:#444}
  .btn.subscribe{left:1000px;top:0;position:absolute}
  .signup .btn{left:834px;top:75px;width:140px;height:47px}
</style>
</head>
<body>
<div class="page">
  <div class="hero-leaves" role="img" aria-label="Dezente Zimmerpflanze im Hintergrund"></div>
  <div class="hero-photo" role="img" aria-label="Foto: Therapeut behandelt Arm und Schulter eines Patienten"></div>

  <div class="topbar">
    <div class="item address">
      <svg width="12" height="13" viewBox="0 0 12 14"><path d="M6 0a5 5 0 0 0-5 5c0 3.6 5 9 5 9s5-5.4 5-9a5 5 0 0 0-5-5zm0 7a2 2 0 1 1 0-4 2 2 0 0 1 0 4z" fill="#fff"/></svg>
      Lindenhofer Straße 14, 33790 Halle
    </div>
    <div class="item mail">
      <svg width="12" height="10" viewBox="0 0 12 10"><rect width="12" height="10" rx="2" fill="#fff"/><path d="M2 3l4 2.5L10 3" stroke="#d5ad14" stroke-width="1.2" fill="none"/></svg>
      info@praxis-vitara.de
    </div>
  </div>

  <header class="header">
    <div class="brand"><span class="dot"></span>Vitara</div>
    <nav class="nav">
      <span>Leistungen <svg width="11" height="7" viewBox="0 0 11 7"><path d="M1 1l4.5 4.5L10 1" stroke="#111" stroke-width="1.6" fill="none"/></svg></span>
      <span>Symtome <svg width="11" height="7" viewBox="0 0 11 7"><path d="M1 1l4.5 4.5L10 1" stroke="#111" stroke-width="1.6" fill="none"/></svg></span>
      <span>Über mich</span>
      <span>Blog</span>
      <span>Kontakt</span>
    </nav>
    <div class="phone">
      <div class="ring"><div class="ball">
        <svg width="14" height="14" viewBox="0 0 24 24"><path d="M6.6 10.8a15.1 15.1 0 0 0 6.6 6.6l2.2-2.2c.3-.3.7-.4 1-.2 1.1.4 2.3.6 3.6.6.6 0 1 .4 1 1V20c0 .6-.4 1-1 1A17 17 0 0 1 3 4c0-.6.4-1 1-1h3.5c.6 0 1 .4 1 1 0 1.3.2 2.5.6 3.6.1.3 0 .7-.2 1z" fill="#fff"/></svg>
      </div></div>
      05421 3088120
    </div>
  </header>

  <p class="tagline"><b>Leidenschaftlicher</b> Physiotherapeut und sektoraler Heilpraktiker.</p>
  <h1 class="headline">ICH LÖSE DEINE<br>SCHMERZEN</h1>
  <p class="intro">Ich bin leidenschaftlicher Physiotherapeut und sektoraler Heilpraktiker. Ich freue mich über Ihren Besuch und hoffe, dass ich Ihnen bei Ihrem Beschwerdebild behilflich sein kann. Buchen Sie jetzt Ihren Termin für die nächste Behandlung.</p>
  <div class="btn book">Termin buchen</div>

  <ul class="dropdown">
    <li><svg width="7" height="11" viewBox="0 0 7 11"><path d="M1 1l4.5 4.5L1 10" stroke="#111" stroke-width="1.4" fill="none"/></svg>Rückenschmerzen</li>
    <li><svg width="7" height="11" viewBox="0 0 7 11"><path d="M1 1l4.5 4.5L1 10" stroke="#111" stroke-width="1.4" fill="none"/></svg>Migräne</li>
    <li><svg width="7" height="11" viewBox="0 0 7 11"><path d="M1 1l4.5 4.5L1 10" stroke="#111" stroke-width="1.4" fill="none"/></svg>Massagen</li>
    <li><svg width="7" height="11" viewBox="0 0 7 11"><path d="M1 1l4.5 4.5L1 10" stroke="#111" stroke-width="1.4" fill="none"/></svg>Tinnitus</li>
    <li><svg width="7" height="11" viewBox="0 0 7 11"><path d="M1 1l4.5 4.5L1 10" stroke="#111" stroke-width="1.4" fill="none"/></svg>Laufanalyse</li>
  </ul>

  <p class="note">Farbkombination variabel</p>

  <section class="infobox">
    <div class="facts">
      <div class="fact loc">
        <svg width="28" height="28" viewBox="0 0 28 28"><path d="M2 2l24 9-11 3-3 11z" stroke="#fff" stroke-width="1.8" fill="none" stroke-linejoin="round"/></svg>
        <h3>Standort</h3>
        <p>Lindenhofer Straße 14<br>33790 Halle</p>
      </div>
      <div class="divider"></div>
      <div class="fact hours">
        <svg width="28" height="28" viewBox="0 0 28 28"><circle cx="14" cy="14" r="12.5" stroke="#fff" stroke-width="1.8" fill="none"/><path d="M14 7v7h6" stroke="#fff" stroke-width="1.8" fill="none"/></svg>
        <h3>Öffnungszeiten</h3>
        <p>09:00 - 17:00 Uhr<br>Montag - Freitag</p>
      </div>
    </div>
    <div class="signup">
      <h3>Für mehr Informationen</h3>
      <div class="field">Deine E-Mail-Adresse</div>
      <div class="btn">Jetzt anmelden</div>
    </div>
  </section>
</div>
</body>
</html>
```